Following list to be designed:

1. A4 Letter Head

Must comprise of:
BRIGHT HARBOR and its LOGO
Address: No.41, 2F, Tarwin Plaza, Melrick Road, Upper Fenwood Gardens, Bangalore 560 017
Tel: 080 27481930
Fax: 080 27481931
Mail: query@brightharbor.example

Color of wordings to be in the lighter shade of blue and brighter shade of blue.

2. A4 Envelope

Must comprise of:
BRIGHT HARBOR and its LOGO
Tel: 080 27481930
Fax: 080 27481931

3. Postal Envelope

Must comprise of:
BRIGHT HARBOR and its LOGO
Tel: 080 27481930
Fax: 080 27481931

4. Business Card

Must comprise of:
Rohan Mehta
Managing Partner
Cell: +91 9487215043
Mail: rohanmehta@brightharbor.example
Tel: 080 27481930
Fax: 080 27481931

5. A4 Letter Head

Must comprise of:
BRIGHT HARBOR CORP. (wording) and BRIGHT HARBOR LOGO (only blue ribbon)

Blue ribbon (BRIGHT HARBOR LOGO) may be placed on Left Top Corner of the A4 Letter Head
and BRIGHT HARBOR CORP. (wording) to be placed on Right Top Corner of the A4 Letter Head

Tel: 080 27481930
Fax: 080 27481931

6. . A4 Envelope

Must comprise of:

Blue ribbon (BRIGHT HARBOR LOGO) may be placed on Left Top Corner of the A4 Envelope
and BRIGHT HARBOR CORP. (wording) to be placed on Right Top Corner of the A4 Envelope
Tel: 080 27481930
Fax: 080 27481931

Target Market(s)

Top IT/ITES Organizations

Industry/Entity Type

Real Estate Development

Font styles to use
Serif
Sans Serif

Colors
33a6d7
0792cd
85cae6

Requirements
Should not have
• Playful font and color

```html
<!DOCTYPE html>
<html lang="en">
<head>
<meta charset="utf-8">
<title>Bright Harbor Stationery</title>
<link href="https://fonts.googleapis.com/css2?family=Open+Sans:wght@400;600&display=swap" rel="stylesheet">
<style>
:root{
  --blue-deep:#3f7fb6;
  --blue-mid:#0792cd;
  --blue-bright:#33a6d7;
  --blue-light:#85cae6;
  --ink:#555a60;
  --ink-soft:#7b8086;
  --paper:#ffffff;
  --board-top:#ededed;
  --board-bottom:#c6c6c6;
}
*{margin:0;padding:0;box-sizing:border-box}
html,body{width:1200px;height:736px;overflow:hidden}
body{font-family:"Open Sans",sans-serif;color:var(--ink);
  background:linear-gradient(var(--board-top),var(--board-bottom));position:relative}
.piece{position:absolute;background:var(--paper);box-shadow:0 1px 3px rgba(0,0,0,.35)}
.brand{position:absolute;display:flex;align-items:center;gap:5px;font-weight:600;
  color:var(--ink);letter-spacing:.02em;white-space:nowrap}
.brand-mark{width:9px;height:9px;background:var(--blue-bright)}
.brand--light{color:#fff}
.brand--light .brand-mark{background:#fff}
.rule{position:absolute;height:1px;background:var(--blue-bright)}
.address,.contacts{position:absolute;font-size:4.2px;line-height:5.4px;color:var(--ink-soft)}
.contacts{text-align:right}
.contacts span{display:flex;align-items:center;justify-content:flex-end;gap:2px}
.ico{width:4px;height:4px;fill:var(--blue-mid)}
.letter-body{position:absolute;left:26px;top:141px;width:254px;font-size:4.2px;line-height:5.5px;color:var(--ink)}
.letter-body p{margin-bottom:4px}
.signer{position:absolute;left:35px;top:306px;font-size:4.2px;line-height:5.4px}
.flap{position:absolute;overflow:visible}
.card-front{left:84px;top:520px;width:94px;height:166px;text-align:center}
.card-name{margin-top:17px;font-size:6px;font-weight:600;color:var(--blue-mid);letter-spacing:.03em}
.card-role{font-size:4px;color:var(--ink-soft);letter-spacing:.05em}
.card-dash{width:9px;height:1px;background:var(--blue-bright);margin:4px auto}
.card-lines{font-size:4.2px;line-height:6px;color:var(--ink)}
.card-lines span{display:flex;align-items:center;justify-content:center;gap:2px}
.card-back{background:radial-gradient(circle at 60% 45%,var(--blue-bright),var(--blue-deep) 85%)}
</style>
</head>
<body>
<svg width="0" height="0" style="position:absolute">
  <defs>
    <symbol id="i-phone" viewBox="0 0 10 10"><path d="M2 1l2 0 1 2.5-1.2 1a6 6 0 0 0 2.7 2.7l1-1.2L10 7v2a1 1 0 0 1-1 1A9 9 0 0 1 0 2a1 1 0 0 1 1-1z"/></symbol>
    <symbol id="i-fax" viewBox="0 0 10 10"><rect x="2" y="0" width="6" height="3"/><rect x="0" y="3.5" width="10" height="5" rx="1"/></symbol>
    <symbol id="i-mail" viewBox="0 0 10 10"><rect x="0" y="2" width="10" height="6"/></symbol>
    <symbol id="i-cell" viewBox="0 0 10 10"><rect x="2.5" y="0" width="5" height="10" rx="1"/></symbol>
    <linearGradient id="flapGrad" x1="0" x2="1" y1="0" y2="0">
      <stop offset="0" stop-color="#3f7fb6"/><stop offset=".5" stop-color="#5ab4e0"/><stop offset="1" stop-color="#3f7fb6"/>
    </linearGradient>
    <linearGradient id="flapGradV" x1="0" x2="0" y1="0" y2="1">
      <stop offset="0" stop-color="#3f7fb6"/><stop offset=".5" stop-color="#5ab4e0"/><stop offset="1" stop-color="#3f7fb6"/>
    </linearGradient>
  </defs>
</svg>

<!-- Letterhead -->
<section class="piece letterhead" style="left:53px;top:80px;width:302px;height:411px">
  <div class="brand" style="right:24px;top:36px;font-size:11px"><i class="brand-mark"></i>BRIGHT HARBOR</div>
  <div class="letter-body">
    <p>A short note of greeting to open the letter.</p>
    <p>This letter is set on the company stationery to show how a typical page reads, with body copy, margins and spacing that keep the layout calm and easy to follow for every reader.</p>
    <p>This letter is set on the company stationery to show how a typical page reads, with body copy, margins and spacing that keep the layout calm and easy to follow for every reader.</p>
    <p>This letter is set on the company stationery to show how a typical page reads, with body copy, margins and spacing that keep the layout calm and easy to follow for every reader.</p>
  </div>
  <div class="signer">Daniel Osterhout<br>Urban Planner</div>
  <div class="rule" style="left:26px;right:25px;top:378px"></div>
  <div class="address" style="left:26px;top:383px">No.41, 2F, Tarwin Plaza<br>Melrick Road, Upper Fenwood Gardens<br>Bangalore 560 017</div>
  <div class="contacts" style="right:25px;top:383px">
    <span><svg class="ico"><use href="#i-phone"/></svg>080 27481930</span>
    <span><svg class="ico"><use href="#i-fax"/></svg>080 27481931</span>
    <span><svg class="ico"><use href="#i-mail"/></svg>query@brightharbor.example</span>
  </div>
</section>

<!-- A4 envelope portrait -->
<svg class="flap" style="left:373px;top:30px" width="302" height="51"><path d="M0 50 L12 5 Q13 0 19 0 L283 0 Q289 0 290 5 L302 50 Z" fill="url(#flapGrad)"/></svg>
<section class="piece envelope-a4" style="left:373px;top:80px;width:302px;height:411px">
  <div class="brand" style="right:26px;top:24px;font-size:11px"><i class="brand-mark"></i>BRIGHT HARBOR</div>
  <div class="rule" style="left:24px;right:26px;top:377px"></div>
  <div class="address" style="left:24px;top:382px">No.41, 2F, Tarwin Plaza<br>Melrick Road, Upper Fenwood Gardens<br>Bangalore 560 017</div>
  <div class="contacts" style="right:26px;top:382px">
    <span><svg class="ico"><use href="#i-phone"/></svg>080 27481930</span>
    <span><svg class="ico"><use href="#i-fax"/></svg>080 27481931</span>
    <span><svg class="ico"><use href="#i-mail"/></svg>query@brightharbor.example</span>
  </div>
</section>

<!-- A4 envelope landscape -->
<svg class="flap" style="left:1101px;top:189px" width="51" height="302"><path d="M0 0 L45 16 Q51 18 51 26 L51 276 Q51 284 45 286 L0 302 Z" fill="url(#flapGradV)"/></svg>
<section class="piece envelope-wide" style="left:691px;top:189px;width:411px;height:302px">
  <div class="brand" style="right:27px;top:22px;font-size:11px"><i class="brand-mark"></i>BRIGHT HARBOR</div>
  <div class="rule" style="left:24px;right:25px;top:270px"></div>
  <div class="address" style="left:24px;top:275px">No.41, 2F, Tarwin Plaza<br>Melrick Road, Upper Fenwood Gardens<br>Bangalore 560 017</div>
  <div class="contacts" style="right:25px;top:275px">
    <span><svg class="ico"><use href="#i-phone"/></svg>080 27481930</span>
    <span><svg class="ico"><use href="#i-fax"/></svg>080 27481931</span>
    <span><svg class="ico"><use href="#i-mail"/></svg>query@brightharbor.example</span>
  </div>
</section>

<!-- Business card front -->
<section class="piece card-front">
  <div class="card-name">ROHAN MEHTA</div>
  <div class="card-role">MANAGING PARTNER</div>
  <div class="card-dash"></div>
  <div class="card-lines">
    <span><svg class="ico"><use href="#i-phone"/></svg>080 27481930</span>
    <span><svg class="ico"><use href="#i-cell"/></svg>+91 9487215043</span>
    <span><svg class="ico"><use href="#i-fax"/></svg>080 27481931</span>
    <span><svg class="ico"><use href="#i-mail"/></svg>rohanmehta@brightharbor.example</span>
  </div>
  <div class="card-dash"></div>
  <div class="card-lines">Tarwin Plaza, No.41, 2F<br>Melrick Road, Upper Fenwood Gardens<br>Bangalore 560 017</div>
</section>

<!-- Business card backs -->
<section class="piece card-back" style="left:270px;top:516px;width:140px;height:80px">
  <div class="brand brand--light" style="left:36px;top:33px;font-size:10px"><i class="brand-mark"></i>BRIGHT HARBOR</div>
</section>
<section class="piece card-back" style="left:190px;top:606px;width:141px;height:78px">
  <div class="brand brand--light" style="left:36px;top:32px;font-size:10px"><i class="brand-mark"></i>BRIGHT HARBOR</div>
</section>
<section class="piece card-back" style="left:346px;top:606px;width:140px;height:78px">
  <div class="brand brand--light" style="right:12px;bottom:10px;font-size:8px"><i class="brand-mark"></i>BRIGHT HARBOR</div>
</section>

<!-- Postal envelope front -->
<section class="piece envelope-postal" style="left:510px;top:546px;width:298px;height:140px">
  <div class="brand" style="left:16px;top:32px;font-size:7px"><i class="brand-mark" style="width:6px;height:6px"></i>BRIGHT HARBOR</div>
  <div class="address" style="left:16px;top:87px">No.41, 2F, Tarwin Plaza<br>Melrick Road, Upper Fenwood Gardens<br>Bangalore 560 017</div>
  <div class="rule" style="left:16px;width:20px;top:106px;background:var(--ink-soft)"></div>
  <div class="address" style="left:16px;top:112px">
    <span style="display:flex;gap:5px"><svg class="ico"><use href="#i-phone"/></svg>080 27481930</span>
    <span style="display:flex;gap:5px"><svg class="ico"><use href="#i-fax"/></svg>080 27481931</span>
    <span style="display:flex;gap:5px"><svg class="ico"><use href="#i-mail"/></svg>query@brightharbor.example</span>
  </div>
</section>

<!-- Postal envelope back -->
<section class="piece envelope-postal-back" style="left:829px;top:542px;width:300px;height:141px;background:linear-gradient(#fafafa,#ececec)">
  <svg style="position:absolute;left:0;top:0" width="300" height="141">
    <path d="M0 141 L150 62 L300 141" fill="none" stroke="#dcdcdc" stroke-width="1"/>
    <path d="M0 0 L22 45 Q25 51 33 51 L267 51 Q275 51 278 45 L300 0 Z" fill="url(#flapGrad)"/>
  </svg>
  <div class="brand brand--light" style="left:118px;top:20px;font-size:7px"><i class="brand-mark" style="width:6px;height:6px"></i>BRIGHT HARBOR</div>
</section>
</body>
</html>
```